Fiscal Sponsorship Program Flyer

We are seeking a designer to create a 1-2 flyer that explains our fiscal sponsorship program. This flyer will be used to recruit new projects that might be interested in utilizing our fiscal sponsorship services. The pertinent information about our program can be found in the attached PDF. For users who cannot access the PDF, please try this link: https://files.brivanto.net/slides/d/7QtR2wXkLmZp9HvCs4YdNe8JfGaUoBi3Tx5Wl0KyRc2s/view?mode=shared

Target Market(s)

New charitable projects that do not yet have their own 501(c)(3) status, and are seeking a fiscal sponsor.

Industry/Entity Type

Nonprofit/Charity

Requirements
Must have
• The flyer must include the language and detail included on the attached PDF. The desire is to reformat this to be more appealing and easy to read.

```html
<!DOCTYPE html>
<html lang="en">
<head>
<meta charset="utf-8">
<title>Keystone Foundation – Fiscal Sponsorship Program</title>
<link href="https://fonts.googleapis.com/css2?family=PT+Serif:wght@400;700&family=Open+Sans:wght@400;600;700&display=swap" rel="stylesheet">
<style>
:root{
  --red:#f0534c;
  --ink:#16171b;
  --dark:#242529;
  --paper:#ffffff;
  --bg:#e7e8ec;
  --text:#4a4a4f;
  --yellow:#f3d46b;
  --blue:#8fb2ea;
  --green:#8fcf9a;
}
*{margin:0;padding:0;box-sizing:border-box}
html,body{width:914px;height:1200px;overflow:hidden;background:var(--bg)}
body{position:relative;font-family:"Open Sans",Arial,sans-serif;color:var(--text)}
.page{position:absolute;top:322px;width:430px;height:556px;background:var(--paper);overflow:hidden;box-shadow:0 4px 14px rgba(0,0,0,.18)}
.page--front{left:18px}
.page--back{left:466px}
.serif{font-family:"PT Serif",Georgia,serif}

/* front */
.front__top{position:absolute;left:0;top:0;width:100%;height:63px;background:var(--ink)}
.front__rule-red{position:absolute;left:53px;top:58px;width:252px;height:7px;background:var(--red);z-index:2}
.front__photo{position:absolute;left:0;top:63px;width:100%;height:295px;background:linear-gradient(160deg,#5a5e66 0%,#c9cbcf 35%,#e7e3d8 60%,#b9ad86 80%,#cfd6c8 100%)}
.front__rule-dark{position:absolute;left:53px;top:353px;width:252px;height:8px;background:var(--ink);z-index:2}
.front__panel{position:absolute;left:0;top:358px;width:100%;height:198px;background:var(--red)}
.front__title{position:absolute;left:53px;top:388px;font-weight:700;font-size:40px;line-height:36px;color:var(--ink);letter-spacing:.5px}
.front__divider{position:absolute;left:53px;top:466px;width:308px;height:1px;background:rgba(255,255,255,.8)}
.front__subtitle{position:absolute;left:53px;top:470px;font-size:29px;line-height:24px;color:#fff}

/* back header */
.back__mission{position:absolute;left:0;top:0;width:215px;height:81px;background:var(--dark);padding:22px 22px 0 22px;color:#fff}
.back__vision{position:absolute;left:215px;top:0;width:215px;height:81px;background:var(--red);padding:22px 22px 0 22px;color:#fff}
.head-label{font-family:"PT Serif",Georgia,serif;font-size:12px;margin-bottom:6px}
.head-copy{font-size:5.4px;line-height:7.4px}
.amp{position:absolute;left:205px;top:33px;width:20px;height:20px;border-radius:50%;background:#fff;border:1.5px solid var(--ink);font-family:"PT Serif",serif;font-size:11px;line-height:17px;text-align:center;color:var(--ink)}

.col{position:absolute;top:96px}
.col--left{left:27px;width:180px}
.col--right{left:221px;width:182px}
h2.sect{font-family:"PT Serif",Georgia,serif;font-weight:700;font-size:11.5px;line-height:14px;color:var(--ink);margin-bottom:8px}
h2.sect em{font-style:normal;color:var(--red)}
h3.q{font-family:"PT Serif",Georgia,serif;font-weight:700;font-size:8px;line-height:10px;color:var(--red);margin-bottom:3px}
p.body{font-size:5.2px;line-height:7.2px;margin-bottom:10px}
.commit{list-style:none}
.commit li{position:relative;padding-left:12px;font-size:5.2px;line-height:7.2px;margin-bottom:7px}
.commit li::before{content:"";position:absolute;left:0;top:1px;width:6px;height:6px;border-radius:50%;background:var(--red)}
.values{list-style:none;margin-top:12px}
.values li{position:relative;padding-left:31px;margin-bottom:9px;min-height:22px}
.values .dot{position:absolute;left:0;top:0;width:20px;height:20px;border-radius:50%;background:var(--red)}
.values .dot svg{position:absolute;left:5px;top:5px}
.values b{display:block;color:var(--red);font-size:5.3px;line-height:7px}
.values span{display:block;font-size:5.2px;line-height:7px}

/* fees */
.fees__title{position:absolute;left:0;top:419px;width:100%;text-align:center;font-family:"PT Serif",Georgia,serif;font-weight:700;font-size:15px;color:var(--ink)}
.fees__band{position:absolute;left:0;top:463px;width:100%;height:93px;background:var(--red)}
.tab{position:absolute;top:451px;height:13px;border-radius:4px 4px 0 0;font-size:7.6px;font-weight:600;line-height:13px;text-align:center;color:var(--ink)}
.tab--basic{left:23px;width:90px;background:var(--yellow)}
.tab--standard{left:141px;width:114px;background:var(--blue)}
.tab--premium{left:284px;width:116px;background:var(--green)}
.tier{position:absolute;top:471px;color:#fff}
.tier--basic{left:31px;width:110px}
.tier--standard{left:153px;width:120px}
.tier--premium{left:290px;width:120px}
.tier h4{font-size:5.6px;font-weight:600;line-height:7px;margin-bottom:3px}
.tier p{font-size:4.4px;line-height:5.6px;margin-bottom:2px}
.tier ul{list-style:none}
.tier li{position:relative;padding-left:6px;font-size:4.3px;line-height:5.4px}
.tier li::before{content:"✓";position:absolute;left:0;top:0;font-size:4.3px}
</style>
</head>
<body>

<section class="page page--front" aria-label="Flyer front">
  <div class="front__top"></div>
  <div class="front__rule-red"></div>
  <div class="front__photo" role="img" aria-label="Photo of a desk with a calculator, a small model house and car, stacks of coins, dollar bills and a magnifying glass, with a person using a phone in the background"></div>
  <div class="front__rule-dark"></div>
  <div class="front__panel"></div>
  <h1 class="front__title serif">KEYSTONE<br>FOUNDATION</h1>
  <div class="front__divider"></div>
  <p class="front__subtitle serif">FISCAL SPONSORSHIP<br>PROGRAM</p>
</section>

<section class="page page--back" aria-label="Flyer back">
  <div class="back__mission">
    <div class="head-label">Mission</div>
    <p class="head-copy">The Keystone Foundation, founded in 2010, exists to support social impact campaigns and organizations through educational, public engagement, and awareness efforts.</p>
  </div>
  <div class="back__vision">
    <div class="head-label">Vision</div>
    <p class="head-copy">Its vision is to strengthen the capacity of the social impact sector and its leaders by providing top-tier fiscal sponsorship services.</p>
  </div>
  <div class="amp">&amp;</div>

  <div class="col col--left">
    <h2 class="sect">What is <em>Fiscal</em> Sponsorship?</h2>
    <h3 class="q">What is fiscal sponsorship?</h3>
    <p class="body">The Keystone Foundation, founded in 2010, exists to support social impact campaigns and organizations through educational, public engagement, and awareness efforts.</p>
    <h3 class="q">What kinds of projects are eligible for fiscal sponsorship?</h3>
    <p class="body">Keystone Foundation uses the following broad criteria to determine whether or not a project is eligible for fiscal sponsorship: 1) mission alignment with the Keystone Foundation; 2) whether or not the project provides an educational, social or charitable benefit; and 3) whether or not the project's activities follow the IRS regulations governing 501(c)(3) public charities.</p>
    <h2 class="sect">Keystone Foundation<br>Program Commitments</h2>
    <ul class="commit">
      <li>Fast, simple and efficient fiscal sponsorship program</li>
      <li>Free and fast approval process - our application can be completed in 30 minutes or less. There is no fee to apply, and most projects can expect to receive a response on their application within 2 weeks</li>
      <li>No fees and no minimums; projects of any size are welcome to apply</li>
      <li>Easy onboarding process</li>
      <li>Dedicated customer service and customization of services, tailored to the individual sponsored project's needs</li>
    </ul>
  </div>

  <div class="col col--right">
    <h2 class="sect">Fiscal Sponsorship Program<br><em>Philosophy</em></h2>
    <p class="body">We believe we can accelerate the pace and scale of social change by providing strategic back office support to emerging projects, leaders and ideas.</p>
    <p class="body">By providing light touch administrative and capacity building services, our fiscal sponsorship program takes the administrative burden off the shoulders of leaders and their projects to allow them to focus on what they do best - achieving impact and changing the world.</p>
    <h2 class="sect" style="margin-top:14px">Organizational Values</h2>
    <ul class="values">
      <li><span class="dot"><svg width="10" height="10" viewBox="0 0 10 10"><path d="M5 1 L8.5 2.5 V5 C8.5 7 7 8.5 5 9 C3 8.5 1.5 7 1.5 5 V2.5 Z" fill="none" stroke="#fff" stroke-width="1"/></svg></span><b>Trust:</b><span>We believe that all successful partnerships begin with a foundation of trust.</span></li>
      <li><span class="dot"><svg width="10" height="10" viewBox="0 0 10 10"><circle cx="3" cy="3" r="1.3" fill="#fff"/><circle cx="7" cy="3" r="1.3" fill="#fff"/><rect x="1.5" y="5" width="7" height="3.5" rx="1" fill="#fff"/></svg></span><b>Relationships:</b><span>Our partners are central to our work. We honor our relationships through respect, communication and transparency.</span></li>
      <li><span class="dot"><svg width="10" height="10" viewBox="0 0 10 10"><circle cx="5" cy="5" r="2.2" fill="none" stroke="#fff" stroke-width="1.2"/><path d="M5 0.5V2M5 8V9.5M0.5 5H2M8 5H9.5" stroke="#fff" stroke-width="1.2"/></svg></span><b>Embrace Complexity and Risk:</b><span>We understand that bold solutions to intractable social issues often require both complexity and risk.</span></li>
      <li><span class="dot"><svg width="10" height="10" viewBox="0 0 10 10"><circle cx="5" cy="4" r="3" fill="none" stroke="#fff" stroke-width="1"/><rect x="3.8" y="7" width="2.4" height="2" fill="#fff"/></svg></span><b>Innovation:</b><span>We embrace continuous improvement, bold creativity and change.</span></li>
      <li><span class="dot"><svg width="10" height="10" viewBox="0 0 10 10"><circle cx="2.5" cy="2.5" r="1.1" fill="#fff"/><circle cx="5" cy="2.5" r="1.1" fill="#fff"/><circle cx="7.5" cy="2.5" r="1.1" fill="#fff"/><rect x="1.6" y="4.2" width="1.8" height="4.5" fill="#fff"/><rect x="4.1" y="4.2" width="1.8" height="4.5" fill="#fff"/><rect x="6.6" y="4.2" width="1.8" height="4.5" fill="#fff"/></svg></span><b>Diversity:</b><span>We believe that all voices matter and that effective solutions are created when decision-making is inclusive across social, cultural and economic backgrounds.</span></li>
    </ul>
  </div>

  <h2 class="fees__title">Fee Structure</h2>
  <div class="fees__band"></div>
  <div class="tab tab--basic">Basic | Fee - 4%</div>
  <div class="tab tab--standard">Standard | Fee - 6%</div>
  <div class="tab tab--premium">Premium | Fee - 10% +</div>

  <div class="tier tier--basic">
    <h4>Limited</h4>
    <ul>
      <li>Project Fund Set-Up</li>
      <li>Administration and Management</li>
      <li>Financial Management</li>
      <li>Grant Proposal Review</li>
      <li>Grant Contract Review</li>
      <li>Project Reporting</li>
      <li>Insurance</li>
      <li>Annual Audit and Form 990</li>
    </ul>
  </div>
  <div class="tier tier--standard">
    <h4>Comprehensive<br>Basic Services +</h4>
    <ul>
      <li>Customized Financial Reporting</li>
      <li>Monthly Financial Statements</li>
      <li>Subgranting/regranting to U.S.-based organizations</li>
      <li>Management of Vendor and Independent Contractors (1099s)</li>
    </ul>
  </div>
  <div class="tier tier--premium">
    <h4>Custom</h4>
    <p>Standard Services + custom services tailored to individual project needs.</p>
    <p>Customization Options:</p>
    <ul>
      <li>Subgranting/regranting to international organizations</li>
      <li>Lobbying Filings</li>
      <li>Project Audit</li>
      <li>Grant Writing Assistance</li>
      <li>One-on-One Coaching</li>
    </ul>
  </div>
</section>

</body>
</html>
```